Norvell Property Services LLC. Commercial & Residential

PROFESSIONAL WINDOW WASHING! professional dryer vent cleaning (prevent fires, $aves money, Lowers your electric bill, save your dryer, less drying time, ask how!)gutter clean outs and tune-up *Lowest Price Quotes Guaranteed!Straightforward Consultancy and Advice to empower homeowners and find solutions that fit your budget!non pressure house cleaning "no pressure...No Damage!Interior & Exterior House Painting call for free in-home consultationPre & Post Tenant Clean-Up PaintGenerator Maintenance Comprehensive Landlord Services & REO (special requests considered) no job too small)!

I would like my business cards to be as professional as possible. I provide property services to commercial and residential clients and need these cards to draw attention and catch ones eye. I have never had business cards for this the services I provide. And I need them so that business owners will trust that our services are the best and also homeowners will call based on the information they see on these cards., I want the window washing service to be the main focal point because it the main service provided. thank you Added Saturday, July 4, 2015

Target Market(s)

Property Services and professional window cleaning highlighted on the front of card rounded edges for card and sleek eye catching cards thank you

Industry/Entity Type

Property Maintenance

Contact Information for Business Card

518-555-0147 Direct. norvellpropertyservicesllc@brindlemail.net

Requirements
Must have
• Professional appearance and eye catch design Property Services as a general point with professional window washing as a highlighted service and all the rest of the services on back of card
Nice to have
• vivid colors but professional appearance

```html
<!DOCTYPE html>
<html lang="en">
<head>
<meta charset="utf-8">
<title>Norvell Property Services LLC – Business Card</title>
<link href="https://fonts.googleapis.com/css2?family=Crimson+Text:wght@700&family=Orbitron:wght@400&family=Quicksand:wght@400&family=Lato:wght@300;400&family=PT+Sans&display=swap" rel="stylesheet">
<style>
  :root {
    --stage: #eef2f7;
    --card-top: #ffffff;
    --card-mid: #e6ebf6;
    --card-bottom: #9fb2df;
    --card-edge: #2fb4e6;
    --title-teal: #15a2ae;
    --tagline-blue: #2d7fd3;
    --contact-ink: #2b2f45;
    --service-violet: #5a4f8e;
    --service-blue: #4a8fd6;
    --slogan-navy: #25306e;
    --water-light: #d9e6f7;
    --water-deep: #6f8fd0;
  }
  * { box-sizing: border-box; margin: 0; padding: 0; }
  html, body { width: 1200px; height: 1000px; overflow: hidden; background: var(--stage); }
  .canvas { position: relative; width: 1200px; height: 1000px; }

  .card {
    position: absolute;
    left: 260px;
    width: 680px;
    height: 400px;
    border-radius: 42px;
    border: 1.5px solid var(--card-edge);
    background: linear-gradient(180deg, var(--card-top) 0%, var(--card-mid) 50%, var(--card-bottom) 100%);
    overflow: hidden;
  }
  .card--front { top: 60px; }
  .card--back { top: 540px; }

  /* Front */
  .brand {
    position: absolute; right: 40px; top: 34px;
    text-align: right;
    font-family: "Crimson Text", serif; font-weight: 700;
    font-size: 27px; line-height: 1.05; color: var(--title-teal);
  }
  .tagline {
    position: absolute; left: 120px; top: 150px;
    font-family: "Orbitron", sans-serif; font-weight: 400;
    font-size: 17px; letter-spacing: 1.5px; color: var(--tagline-blue);
  }
  .window-art {
    position: absolute; left: 0; top: 0; width: 680px; height: 400px;
  }
  .contact {
    position: absolute; left: 44px; top: 300px;
    font-family: "Quicksand", sans-serif; font-size: 15px;
    line-height: 1.55; color: var(--contact-ink); letter-spacing: 0.5px;
  }

  /* Back */
  .services {
    position: absolute; left: 46px; top: 50px;
    font-family: "Lato", sans-serif; font-weight: 300;
  }
  .services__heading { font-size: 15px; color: var(--service-violet); margin-bottom: 2px; }
  .services__list { list-style: none; padding-left: 58px; font-size: 15.5px; line-height: 1.2; color: var(--service-blue); }
  .slogans {
    position: absolute; left: 0; right: 0; top: 205px;
    text-align: center; font-family: "PT Sans", sans-serif; color: var(--slogan-navy);
    padding-left: 120px;
  }
  .slogans__small { font-size: 12px; }
  .slogans__guarantee { font-size: 14px; margin-top: 2px; }
  .slogans__consult { font-size: 19px; margin-top: 3px; }
  .slogans__headline { font-size: 28px; margin-top: 6px; }
</style>
</head>
<body>
<main class="canvas">
  <section class="card card--front">
    <svg class="window-art" viewBox="0 0 680 400" role="img" aria-label="Illustration of a window squeegee sweeping a splash of water across the card">
      <defs>
        <linearGradient id="splash" x1="0" y1="1" x2="1" y2="0">
          <stop offset="0" stop-color="var(--water-light)" stop-opacity="0.2"/>
          <stop offset="1" stop-color="var(--water-deep)" stop-opacity="0.7"/>
        </linearGradient>
      </defs>
      <path d="M40 400 C200 360 380 300 520 250 C580 230 630 215 680 205 L680 400 Z" fill="url(#splash)"/>
    </svg>
    <h1 class="brand">Norvell Property Services LLC.<br>Commercial &amp; Residential</h1>
    <p class="tagline">PROFESSIONAL WINDOW CLEANING SERVICE</p>
    <p class="contact">Phone: (518) 555-0147<br>norvellpropertyservicesllc@brindlemail.net</p>
  </section>

  <section class="card card--back">
    <div class="services">
      <p class="services__heading">Services we provide</p>
      <ul class="services__list">
        <li>Pre &amp; Post Tenant Clean-Up Paint</li>
        <li>Interior &amp; Exterior House Painting</li>
        <li>Generator Maintenance</li>
        <li>Comprehensive Landlord Services</li>
        <li>&amp; REO (special requests considered)</li>
      </ul>
    </div>
    <div class="slogans">
      <p class="slogans__small">No pressure...No Damage!</p>
      <p class="slogans__guarantee">Lowest Price Quotes Guaranteed!</p>
      <p class="slogans__consult">call for free in-home consultation</p>
      <p class="slogans__headline">No job is too small!</p>
    </div>
  </section>
</main>
</body>
</html>
```